Website for boutique digital agency helping high-tech startups accelerate growth.

We need a website design for a relatively young company based in Mauritius called 'LumaTrel'.

We are a professional services firm delivering digital infrastructure for revenue operations (RevOps)*.

Entrepreneurial startups and SMBs in the technology sector work with us to accelerate growth by delivering extraordinary customer experiences across the full customer lifecycle.

We would like a colourful design that utilises the (4) colours of our existing logo design.

The final design should communicate dynamic growth through relentless customer focus.
----------------------------------------------------------
*Revenue Operations (RevOps) is the strategic alignment of sales, marketing and customer success operations to accelerate growth by delivering extraordinary customer experiences across the full customer life cycle.

Target Market(s)

Entrepreneurial startups and SMBs (Small/Medium Businesses) in the technology sector.

Question: Why the technology sector?

Answer: Because technology entrepreneurs often have a tremendous challenge to effectively communicate to the market and to prospective customers the value and the benefits of their products & services due to the inherent complexity of technological innovation.

LumaTrel is a team of creatively-minded engineers and technologists who have worked with and understand the technologies and innovations our clients are passionate about bringing to market.

Industry/Entity Type

Professional Service

Number of Pages Required

5+ page

Font styles to use
Sans Serif

Requirements
Must have
• Minimalistic designs rich with visual meaning are highly preferred. Mobile responsive designs are also required. Must show how designs render on Desktop, Tablet and Smartphone devices.

Website pages:
1) Homepage: problem statement, target customers, value proposition & benefits
2) Services: 3-4 tiers of services packages with pricing and "how to work with us"
3) Resources: links to all kinds of relevant materials
4) Contact Us: contact form and special project quote form
5) Blog: matrix design with featured images for each post
Nice to have
• Bold, interesting, colourful, inspiring images that visually communicate:
- relentless customer focus
- extraordinary, memorable experiences
- business at the speed of innovation
Should not have
• Any meme or theme that panders to "political correctness".

```html
<!DOCTYPE html>
<html lang="en">
<head>
<meta charset="UTF-8">
<title>LumaTrel — RevOps Simplifies Everything</title>
<link href="https://fonts.googleapis.com/css2?family=Jost:wght@400;500;600&display=swap" rel="stylesheet">
<style>
  :root {
    --ink: #2b333d;
    --red: #ff0036;
    --green: #7cc424;
    --teal: #168080;
    --orange: #ff6a10;
    --pink: #f7b3c3;
    --slate: #3f3d56;
    --white: #ffffff;
  }
  * { margin: 0; padding: 0; box-sizing: border-box; }
  html, body { width: 1200px; height: 675px; overflow: hidden; background: var(--white); }
  body { position: relative; font-family: "Jost", sans-serif; color: var(--ink); }

  .accent-band {
    position: absolute; border-radius: 6px;
    background: linear-gradient(120deg, var(--green) 0%, var(--teal) 50%, var(--red) 80%, var(--orange) 100%);
    opacity: 0.85;
  }
  .accent-band--top { left: 350px; top: 0; width: 142px; height: 50px; }
  .accent-band--bottom { left: 392px; top: 626px; width: 124px; height: 49px; }

  .brand {
    position: absolute; left: 88px; top: 50px;
    font-weight: 600; font-size: 24px; color: var(--ink); letter-spacing: 0.2px;
  }

  .main-nav { position: absolute; top: 52px; right: 88px; display: flex; gap: 31px; }
  .main-nav a {
    font-size: 16.5px; color: var(--ink); text-decoration: none; letter-spacing: 0.3px;
    padding-bottom: 3px; border-bottom: 1.5px solid transparent;
  }
  .main-nav a.is-active { border-bottom-color: var(--ink); }

  .section-nav { position: absolute; left: 0; top: 0; }
  .section-nav a {
    position: absolute; white-space: nowrap; font-size: 16.5px; color: var(--ink);
    text-decoration: none; letter-spacing: 0.3px; transform: translateY(-50%);
  }
  .section-index {
    position: absolute; left: 68px; top: 374px; transform: translateY(-50%);
    font-size: 32px; font-weight: 600; color: var(--pink); letter-spacing: 1px;
  }
  .section-nav a.is-current { font-size: 21.5px; font-weight: 600; letter-spacing: 0.8px; }

  .hero-copy { position: absolute; left: 405px; top: 187px; width: 336px; }
  .hero-title { font-size: 31px; font-weight: 600; line-height: 38px; letter-spacing: 0.8px; }
  .hero-text { margin-top: 9px; font-size: 17.3px; line-height: 18.75px; letter-spacing: 0.15px; }
  .hero-cta {
    display: inline-flex; align-items: center; justify-content: center;
    margin-top: 36px; width: 163px; height: 50px; border-radius: 10px;
    background: var(--red); color: var(--white); font-size: 17px; font-weight: 500;
    text-decoration: none; letter-spacing: 0.3px;
  }

  .hero-illustration {
    position: absolute; left: 777px; top: 267px; width: 335px; height: 141px;
    border-radius: 8px;
    background: linear-gradient(100deg, var(--slate) 0%, var(--slate) 28%, var(--red) 40%, #e0002f 85%, var(--slate) 100%);
  }
</style>
</head>
<body>
  <div class="accent-band accent-band--top" role="img" aria-label="Decorative diagonal stripes in green, teal and red"></div>
  <div class="accent-band accent-band--bottom" role="img" aria-label="Decorative diagonal stripes in green, orange, teal and red"></div>

  <div class="brand">lumatrel.io</div>

  <nav class="main-nav">
    <a href="#" class="is-active">Home</a>
    <a href="#">Services</a>
    <a href="#">Resources</a>
    <a href="#">Contact Us</a>
    <a href="#">Blog</a>
  </nav>

  <nav class="section-nav">
    <a href="#" style="left:118px; top:252px;">Home</a>
    <a href="#" style="left:118px; top:293px;">Problem Statement</a>
    <a href="#" style="left:118px; top:333px;">Target Customers</a>
    <span class="section-index">04</span>
    <a href="#" class="is-current" style="left:117px; top:380px;">Value Proposition</a>
    <a href="#" style="left:117px; top:424px;">Benefits</a>
  </nav>

  <section class="hero-copy">
    <h1 class="hero-title">RevOps Simplifies Everything</h1>
    <p class="hero-text">Most companies have legacy org structures based on how businesses were run twenty years ago. New functions have been added into this structure over time, creating leadership roles that are overly broad. RevOps consolidates operations into one team to simplify everything.</p>
    <a href="#" class="hero-cta">Learn More</a>
  </section>

  <div class="hero-illustration" role="img" aria-label="Illustration of a person sitting beside a large laptop with a red screen and floating squares"></div>
</body>
</html>
```